EXTENDED Store hours to serve your healthcare needs

I'M LOOKING FOR A NICE FLYER THAT SHOWS THE FOLLOWING INFORMATION:

Logo
address
tel phone and fax
email address

Extending our hours to meet the growing healthcare needs of our community. Fast delivery service!

Monday - Thursday 10am-midnight
Friday 10am-4pm
Saturday - Motzei Shabbos till midnight
Sunday 10am-7pm

Target Market(s)

Community

Industry/Entity Type

Pharmacy

Requirements
Must have
• Extended hours
• personal care
• expert advice
• superior service
Nice to have
• Looking for no people pictures
• Eye popping design
• Classic modern clean design
Should not have
• store description is services
• And should not say Fiirst to open and last to close

```html
<!DOCTYPE html>
<html lang="en">
<head>
<meta charset="utf-8">
<title>Lindell Pharmacy – New Store Hours</title>
<link href="https://fonts.googleapis.com/css2?family=Kaushan+Script&family=Roboto+Condensed:wght@400&family=Open+Sans:wght@400;600&family=Oxygen:wght@300;400&display=swap" rel="stylesheet">
<style>
  :root{
    --page:#e4e2df;
    --paper:#ececec;
    --blue:#2c55a6;
    --red:#b01f26;
    --panel:#c5d3ee;
    --slate:#6b6b6b;
    --ink:#1d1d1d;
    --gold:#f0cf78;
  }
  *{margin:0;padding:0;box-sizing:border-box}
  html,body{width:1200px;height:1076px;overflow:hidden;background:var(--page)}
  .flyer{position:absolute;left:247px;top:38px;width:705px;height:1000px;background:var(--paper);overflow:hidden;box-shadow:0 6px 18px rgba(0,0,0,.18)}
  .flyer-art{position:absolute;inset:0;width:705px;height:1000px}
  .brand-dot{position:absolute;left:112px;top:98px;width:88px;height:88px;border-radius:50%;background:var(--blue)}
  .brand-name{position:absolute;left:222px;top:36px;font-family:"Roboto Condensed",sans-serif;font-weight:400;color:var(--red);font-size:136px;line-height:1;white-space:nowrap}
  .brand-type{position:absolute;left:432px;top:192px;font-family:"Roboto Condensed",sans-serif;font-weight:400;color:var(--blue);font-size:44px;letter-spacing:5px;line-height:1;white-space:nowrap}
  .hours-title{position:absolute;left:300px;top:578px;width:270px;transform:rotate(3deg);text-align:center;font-family:"Open Sans",sans-serif;font-weight:600;font-size:24px;color:var(--gold);letter-spacing:-.3px}
  .day-block{position:absolute;text-align:center;color:var(--ink)}
  .day-name{font-family:"Kaushan Script",cursive;font-size:37px;line-height:1.1;white-space:nowrap}
  .day-time{font-family:"Oxygen",sans-serif;font-weight:300;font-size:23px;letter-spacing:.8px;margin-top:4px;white-space:nowrap}
  .day-note{font-family:"Oxygen",sans-serif;font-weight:300;font-size:25px;font-variant:small-caps;letter-spacing:1px;line-height:.95;text-align:left;margin-top:6px;margin-left:-4px;white-space:nowrap}
  .mon-thu{left:268px;top:660px;width:270px}
  .friday{left:575px;top:660px;width:140px}
  .saturday{left:318px;top:800px;width:170px}
  .sunday{left:582px;top:804px;width:125px}
  .contact{position:absolute;left:16px;top:756px;font-family:"Open Sans",sans-serif;font-size:14.5px;color:var(--ink);list-style:none}
  .contact li{display:flex;align-items:flex-start;gap:10px;margin-bottom:10px;line-height:1.55}
  .contact svg{flex:none;width:24px;height:20px;margin-top:1px}
</style>
</head>
<body>
<main class="flyer">
  <svg class="flyer-art" viewBox="0 0 645 915" preserveAspectRatio="none">
    <defs>
      <radialGradient id="tabletTone" cx="0.35" cy="0.35" r="0.8">
        <stop offset="0" stop-color="#efd3d8"/>
        <stop offset="0.5" stop-color="#e7dddd"/>
        <stop offset="1" stop-color="#d9d9d9"/>
      </radialGradient>
      <radialGradient id="pillsTone" cx="0.4" cy="0.4" r="0.7">
        <stop offset="0" stop-color="#e6d4cc"/>
        <stop offset="1" stop-color="#ececec"/>
      </radialGradient>
      <linearGradient id="portraitTone" x1="0" y1="0" x2="0" y2="1">
        <stop offset="0" stop-color="#efe6d8"/>
        <stop offset="0.5" stop-color="#e8d6b8"/>
        <stop offset="1" stop-color="#f4f4f4"/>
      </linearGradient>
    </defs>
    <rect class="paper" width="645" height="915" fill="#ececec"/>
    <path role="img" aria-label="Close-up photo of a pink tablet" d="M0,0 H645 V240 Q300,520 0,330 Z" fill="url(#tabletTone)"/>
    <rect role="img" aria-label="Faint photo of scattered capsules and pills" x="0" y="470" width="260" height="380" fill="url(#pillsTone)"/>
    <path class="swoosh-red" d="M0,210 Q300,480 645,185 L645,240 Q300,520 0,330 Z" fill="#b01f26"/>
    <path class="swoosh-blue" d="M0,300 Q300,440 645,230 L645,330 Q420,560 0,455 Z" fill="#2c55a6"/>
    <rect role="img" aria-label="Photo of a smiling pharmacist in a white coat" x="500" y="385" width="145" height="160" fill="url(#portraitTone)"/>
    <polygon class="hours-panel" points="230,500 645,520 645,840 270,860" fill="#c5d3ee"/>
    <polygon class="hours-edge" points="215,545 231,545 271,860 257,860" fill="#2c55a6"/>
    <polygon class="hours-tab" points="268,488 545,515 510,603 265,590" fill="#6b6b6b"/>
    <path class="base-red" d="M0,840 Q380,850 645,812 L645,830 Q380,880 0,882 Z" fill="#b01f26"/>
    <path class="base-blue" d="M0,880 Q360,872 645,812 L645,915 L0,915 Z" fill="#2c55a6"/>
  </svg>

  <span class="brand-dot"></span>
  <span class="brand-name">Lindell</span>
  <span class="brand-type">PHARMACY</span>

  <div class="hours-title">NEW STORE HOURS!</div>

  <div class="day-block mon-thu">
    <div class="day-name">Monday&nbsp; Thursday</div>
    <div class="day-time">10AM-MIDNIGHT</div>
  </div>
  <div class="day-block friday">
    <div class="day-name">Friday</div>
    <div class="day-time">10AM-4PM</div>
  </div>
  <div class="day-block saturday">
    <div class="day-name">Saturday</div>
    <div class="day-note">Motzei-midnight<br>Shabbos</div>
  </div>
  <div class="day-block sunday">
    <div class="day-name">Sunday</div>
    <div class="day-time">10AM-7PM</div>
  </div>

  <ul class="contact">
    <li>
      <svg viewBox="0 0 24 20" aria-hidden="true"><rect x="1" y="1" width="22" height="18" rx="7" fill="none" stroke="#1d1d1d" stroke-width="1.6"/><path d="M6,8 Q12,3 18,8 L16,10 H8 Z M8,10 V15 H16 V10" fill="#1d1d1d"/></svg>
      <span>555-014-2290</span>
    </li>
    <li>
      <svg viewBox="0 0 24 20" aria-hidden="true"><rect x="1" y="1" width="22" height="18" rx="7" fill="none" stroke="#1d1d1d" stroke-width="1.6"/><path d="M12,4 C8.5,4 7,7 8,9.5 L12,16 L16,9.5 C17,7 15.5,4 12,4 Z" fill="none" stroke="#1d1d1d" stroke-width="1.5"/><circle cx="12" cy="8" r="1.6" fill="#1d1d1d"/></svg>
      <span>48 Maple Row Brookfield,<br>NY 10950</span>
    </li>
    <li>
      <svg viewBox="0 0 24 20" aria-hidden="true"><rect x="1" y="1" width="22" height="18" rx="7" fill="none" stroke="#1d1d1d" stroke-width="1.6"/><rect x="6" y="6" width="12" height="8" fill="none" stroke="#1d1d1d" stroke-width="1.4"/><path d="M6,6 L12,11 L18,6" fill="none" stroke="#1d1d1d" stroke-width="1.4"/></svg>
      <span>lindellpharmacy@mailbox.com</span>
    </li>
  </ul>
</main>
</body>
</html>
```